Business Card for my Photography/Video Business

I would like the card to say Event Photographer and Videographer. I like the Black and Gold look to it as well but open to other options. I don't want it to be super vibrant or colorful. Simple, elegant and professional

```html
<!DOCTYPE html>
<html lang="en">
<head>
<meta charset="utf-8">
<title>Orrin Studio – Business Card</title>
<link rel="stylesheet" href="https://fonts.googleapis.com/css2?family=Lato:wght@400;700&display=swap">
<style>
  :root {
    --backdrop: #666666;
    --card-light: #f6f6f6;
    --card-dark: #1c1c1c;
    --gold: #c4a03a;
    --gold-text: #b8932c;
    --ink: #1e1e1e;
    --divider: #c9c9c9;
    --icon-cut: #f6f6f6;
  }
  * { margin: 0; padding: 0; box-sizing: border-box; }
  html, body {
    width: 1200px; height: 802px; overflow: hidden;
    background: var(--backdrop);
    font-family: "Lato", Arial, sans-serif;
  }
  .card {
    position: absolute; top: 274px;
    width: 443px; height: 265px;
  }
  .card--front { left: 136px; background: var(--card-light); }
  .card--back { left: 624px; background: var(--card-dark); }

  .brand-name {
    position: absolute;
    color: var(--gold);
    font-weight: 400;
    line-height: 1;
    white-space: nowrap;
  }
  .card--front .brand-name {
    left: 26px; top: 120px;
    font-size: 28px;
  }
  .card--back .brand-name {
    left: 0; right: 0; top: 112px;
    text-align: center;
    font-size: 40px;
  }

  .divider {
    position: absolute; left: 231px; top: 81px;
    width: 1px; height: 105px; background: var(--divider);
  }
  .contact { position: absolute; left: 253px; top: 86px; color: var(--ink); }
  .contact__name {
    font-size: 16.5px; font-weight: 400; color: var(--gold-text);
    letter-spacing: 0.01em; line-height: 18px;
  }
  .contact__role { font-size: 12.5px; line-height: 14px; }
  .contact__list { list-style: none; margin-top: 17px; }
  .contact__item {
    display: flex; align-items: center;
    font-size: 12.8px; line-height: 16px;
  }
  .contact__icon { width: 10px; height: 10px; margin-right: 5px; fill: var(--gold); flex: none; }
</style>
</head>
<body>
  <section class="card card--front">
    <span class="brand-name">Orrin Studio</span>
    <span class="divider"></span>
    <div class="contact">
      <h1 class="contact__name">DANIEL REYES</h1>
      <p class="contact__role">Managing Director</p>
      <ul class="contact__list">
        <li class="contact__item">
          <svg class="contact__icon" viewBox="0 0 10 10"><path d="M1 3.5C1 2 2 1.5 5 1.5S9 2 9 3.5L7.5 4 7 3H3L2.5 4Z"/><rect x="2" y="4.5" width="6" height="4" rx="0.8"/></svg>
          044-987 654 321
        </li>
        <li class="contact__item">
          <svg class="contact__icon" viewBox="0 0 10 10"><rect x="0.5" y="2" width="9" height="6.5"/><path d="M0.5 2 5 5.5 9.5 2" fill="none" stroke="var(--icon-cut)" stroke-width="0.9"/></svg>
          hello@orrinstudio.com
        </li>
        <li class="contact__item">
          <svg class="contact__icon" viewBox="0 0 10 10"><circle cx="5" cy="5" r="4.5"/><path d="M3 3.5 5 3 5.5 5 4 6.5M6.5 7 7.5 5.5" fill="none" stroke="var(--icon-cut)" stroke-width="0.8"/></svg>
          www.orrinstudio.com
        </li>
      </ul>
    </div>
  </section>

  <section class="card card--back">
    <span class="brand-name">Orrin Studio</span>
  </section>
</body>
</html>
```